Registry Program Flyer Design 1 - QWVT registry

We need two different flyers that will be distributed via web, email and print. This project is for one of the two flyers.

The audience is patients and family members of patients with a specific disease. The flyer will be used to make patients aware of our web-based registry programs, and to inform/encourage patients to join.

An example prototype flyer with the text that should be used is attached. We would like to improve the design and layout of the flyers, while retaining as much of the language as appropriate.

For this project, the flyer may use the pictures included in the prototype, however, it is not required.

If possible, a final format that allows us to edit the text is preferred. If this is not possible, we will finalize the text after receiving a prototype. Changes to the text will likely be minor.

Note: The design of the flyers for this project and the other project (Registry Program Flyer design 2 - Orvia Link registry) can be similar in style, however, they should not be duplicates.

Final deliverable should be in a .PSD format (photoshop) with layers so we can edit text if necessary.

Target Market(s)

Physicians and healthcare providers

Requirements
Must have
• Use the attached logo file and color scheme.

```html
<!DOCTYPE html>
<html lang="en">
<head>
<meta charset="utf-8">
<title>QWVT Link – Registry Flyer</title>
<link href="https://fonts.googleapis.com/css2?family=Arimo:wght@400;700&family=Source+Sans+3:wght@400;600&display=swap" rel="stylesheet">
<style>
  :root{
    --brand-blue:#1b8bcb;
    --heading-blue:#2790d2;
    --orange:#f07a22;
    --ink:#333333;
    --ink-soft:#555555;
    --rule:#c9c9c9;
    --page:#ffffff;
    --backdrop:#e9eaec;
  }
  *{box-sizing:border-box;margin:0;padding:0}
  html,body{width:990px;height:1200px;overflow:hidden;background:var(--backdrop)}
  body{font-family:"Arimo",Arial,sans-serif;color:var(--ink)}

  .flyer{position:absolute;left:55px;top:9px;width:880px;height:1182px;background:var(--page);overflow:hidden;box-shadow:0 2px 10px rgba(0,0,0,.18)}

  /* Header */
  .brand{position:absolute;left:40px;top:40px;display:flex;flex-direction:column}
  .brand-name{font-family:"Source Sans 3",sans-serif;font-weight:400;font-size:36px;color:var(--brand-blue);letter-spacing:1px;line-height:1}
  .brand-url{font-weight:700;font-size:15px;letter-spacing:2px;color:var(--ink-soft);margin-top:10px}
  .header-rule{position:absolute;left:428px;top:24px;width:1px;height:100px;background:var(--rule)}
  .tagline{position:absolute;left:446px;top:26px;font-family:"Source Sans 3",sans-serif;font-size:26px;line-height:1.22;color:var(--ink);letter-spacing:.5px}

  /* Photos */
  .photo{position:absolute;top:136px;height:250px}
  .photo-team{left:0;width:455px;background:linear-gradient(180deg,#f4f6f8 0%,#dfe6ec 55%,#c7d3dd 100%)}
  .photo-consult{left:458px;width:422px;background:linear-gradient(160deg,#e7ecef 0%,#cfd9e1 50%,#b9c8d5 100%)}
  .photo-band{position:absolute;left:0;top:386px;width:880px;height:10px;background:var(--brand-blue)}
  .photo-band-accent{position:absolute;left:0;top:396px;width:880px;height:4px;background:var(--orange)}

  /* Columns */
  .column{position:absolute;top:448px}
  .column-left{left:40px;width:405px}
  .column-right{left:496px;width:350px}
  .column-rule{position:absolute;left:470px;top:448px;width:1px;height:590px;background:#dcdcdc}
  .section-title{font-weight:700;font-size:18px;color:var(--heading-blue);margin-bottom:10px}
  .column p{font-size:14px;line-height:1.32;margin-bottom:14px}
  .bullets{list-style:none;margin-bottom:12px}
  .bullets li{position:relative;padding-left:18px;font-size:14px;line-height:1.3}
  .bullets li::before{content:"";position:absolute;left:2px;top:5px;width:8px;height:8px;border-radius:50%;background:var(--orange)}
  .bullets-spaced li{margin-bottom:2px}

  /* Footer */
  .footer-accent{position:absolute;left:0;top:1058px;width:880px;height:6px;background:var(--orange)}
  .footer{position:absolute;left:0;top:1064px;width:880px;height:118px;background:var(--brand-blue);color:#fff;text-align:center}
  .footer-slogan{font-family:"Source Sans 3",sans-serif;font-weight:600;font-size:31px;margin-top:24px;letter-spacing:.3px}
  .footer-contact{font-size:14px;margin-top:10px}
  .footer-contact span{margin:0 8px}
</style>
</head>
<body>
<div class="flyer">

  <header>
    <div class="brand">
      <div class="brand-name">QWVT Link</div>
      <div class="brand-url">www.QWVTlink.org</div>
    </div>
    <div class="header-rule"></div>
    <div class="tagline">Connecting patients,<br>healthcare professionals,<br>researchers &amp; policy makers</div>
  </header>

  <div class="photo photo-team" role="img" aria-label="Smiling team of doctors and nurses in white coats"></div>
  <div class="photo photo-consult" role="img" aria-label="Doctor talking with a patient at a desk"></div>
  <div class="photo-band"></div>
  <div class="photo-band-accent"></div>

  <section class="column column-left">
    <h2 class="section-title">Who Can Benefit</h2>
    <ul class="bullets">
      <li>Patients</li>
      <li>Healthcare providers</li>
      <li>Researchers</li>
      <li>Industry representatives</li>
      <li>Policy-makers</li>
      <li>All stakeholders interested in QWVT</li>
    </ul>

    <h2 class="section-title">How it Works</h2>
    <p>Patients can join the registry to submit their data. After taking web-based surveys, explore the collected information in a way that protects the privacy of everyone.</p>

    <h2 class="section-title">Who We Are</h2>
    <p>The Halvern Lipid Research Foundation (HLRF) reviewed the registry survey. As a professional organization, our mission has been to reduce the morbidity and mortality from cardiovascular disease by increasing the understanding of the pathophysiology, and detection and optimal treatment of lipid disorders.</p>
    <p>CareJunction pioneered the LINKWAY registry platform, which allows patients around the world to join others in reporting their own experience of disease. In use since 2007, our registries collect data from patients for over 350 diseases worldwide for foundations, companies and governments.</p>
  </section>

  <div class="column-rule"></div>

  <section class="column column-right">
    <h2 class="section-title">Get Connected.</h2>
    <p>It takes whole communities to help people living with medical conditions lead healthier and happier lives. The LINKWAY QWVT Registry brings together individuals affected by quinary wave vascular tension and professionals involved in their medical care and research.</p>
    <p>Join THE LINKWAY QWVT Registry to:</p>
    <ul class="bullets bullets-spaced">
      <li>Learn how other patients manage their health</li>
      <li>Take surveys and share your experiences in a program that safeguards your privacy</li>
      <li>Receive information about opportunities to participate in research</li>
      <li>Help researchers unlock more effective treatments</li>
      <li>Help healthcare providers better understand QWVT</li>
      <li>Improve knowledge about patient communities among advocacy groups</li>
    </ul>
    <p>The more data we collect about an illness, the closer we can get to helping communities find treatments that work. Your participation is crucial to help reach the goal of developing more effective treatments for QWVT.</p>
    <p>Encourage everyone you know to join today!</p>
  </section>

  <div class="footer-accent"></div>
  <footer class="footer">
    <div class="footer-slogan">Learn from others... Make a difference.... Get Connected</div>
    <div class="footer-contact">
      www.QWVTRegistry.org<span>|</span>info@carejunction.org<span>|</span>Copyright © 2014 CareJunction
    </div>
  </footer>

</div>
</body>
</html>
```